Electrical business card

I require a business card for my company I will attach my log. My business is a electrical business. I would like the card to have a smart corporate look nothing to over the top.

Industry/Entity Type

Business

```html
<!DOCTYPE html>
<html lang="en">
<head>
<meta charset="utf-8">
<title>Brightline Power – Business Card</title>
<link rel="stylesheet" href="https://fonts.googleapis.com/css2?family=Oswald:wght@400;500;600&display=swap">
<style>
  :root{
    --page:#e9e6e2;
    --card-white:#ffffff;
    --card-black:#050505;
    --ink:#111111;
    --accent:#4fb8e8;
    --accent-soft:#8fd3f2;
    --logo-grey:#b9bec4;
  }
  *{box-sizing:border-box;margin:0;padding:0}
  html,body{width:800px;height:1200px;overflow:hidden}
  body{background:var(--page);font-family:"Oswald",sans-serif;color:var(--ink);position:relative}

  .card{position:absolute;width:700px;height:390px;overflow:hidden;box-shadow:0 8px 22px rgba(0,0,0,.25)}
  .card--front{left:37px;top:226px;background:var(--card-white)}
  .card--back{left:80px;top:652px;height:396px;background:var(--card-black)}

  .holder{position:absolute;top:22px;left:0;right:0;text-align:center}
  .holder__name{font-size:38px;font-weight:600;letter-spacing:.5px;line-height:1.1}
  .holder__rule{width:270px;height:1px;background:#cfcfcf;margin:6px auto 4px}
  .holder__position{font-size:17px;font-weight:400;color:var(--accent);letter-spacing:.5px}

  .contact{position:absolute;display:grid;grid-template-columns:auto auto;column-gap:6px;align-items:baseline}
  .contact dt{font-weight:600;text-align:right;color:var(--ink)}
  .contact dd{font-weight:400;color:var(--accent)}
  .contact--main{left:20px;top:160px;font-size:22px;row-gap:2px}
  .contact--office{left:420px;top:160px;font-size:15px;row-gap:1px}

  .band{position:absolute;left:0;right:0;bottom:0;height:94px;background:var(--card-black);display:flex;align-items:center;padding-left:40px}

  .brand{display:flex;align-items:center;gap:14px;font-family:"Oswald",sans-serif;font-weight:400;color:var(--logo-grey);letter-spacing:4px;text-transform:uppercase;white-space:nowrap}
  .brand__dot{width:30px;height:30px;border-radius:50%;background:var(--accent)}
  .band .brand{font-size:50px}
  .card--back .brand{position:absolute;left:0;right:0;top:150px;justify-content:center;font-size:62px}

  .glow{position:absolute;left:30px;right:30px;top:262px;height:3px;border-radius:2px;
    background:linear-gradient(90deg,transparent,var(--accent) 25%,var(--accent-soft) 50%,var(--accent) 75%,transparent);
    box-shadow:0 0 14px 4px rgba(79,184,232,.55)}
</style>
</head>
<body>
  <section class="card card--front" aria-label="Business card front">
    <header class="holder">
      <h1 class="holder__name">CARD HOLDER NAME</h1>
      <div class="holder__rule"></div>
      <p class="holder__position">POSITION</p>
    </header>

    <dl class="contact contact--main">
      <dt>Phone:</dt><dd>715230968812</dd>
      <dt>Email:</dt><dd>info@brtpwr.com</dd>
      <dt>Fax:</dt><dd>4415098276</dd>
    </dl>

    <dl class="contact contact--office">
      <dt>Street:</dt><dd>12 Harbor Lane</dd>
      <dt>Phone:</dt><dd>13579246801</dd>
      <dt>Email:</dt><dd>desk@brtpwr.com</dd>
      <dt>Fax:</dt><dd>31459026</dd>
    </dl>

    <div class="band">
      <div class="brand"><span class="brand__dot"></span>Brightline Power</div>
    </div>
  </section>

  <section class="card card--back" aria-label="Business card back">
    <div class="brand"><span class="brand__dot"></span>Brightline Power</div>
    <div class="glow"></div>
  </section>
</body>
</html>
```